Brightpath Wellness Referral Program

We have recently started a referral program for our clinics and we need a postcard that we can hand our to clients to let them know about the new program.
We are looking for a 4x6" card design that highlights our incentive referral program while visually either showing some of the services we offer, or, conveying a message of health, community, family, etc.
The details of our referral program can be found at:
https://brightpathwellness.ca/about/refer-a-friend.html
We would also like to see somewhere on the card, 2 lines for:
1) Your name: ( new clients name)
2) Referred by: __________
The card can be single or double sided, whatever looks best for design purposes.
Target Market(s)
Ages 20-50, equal men and women
Look and feel
Each slider illustrates characteristics of the customer's brand and the style your logo design should communicate.

```html
<!DOCTYPE html>
<html lang="en">
<head>
<meta charset="utf-8">
<title>Brightpath Wellness Referral Postcard</title>
<link href="https://fonts.googleapis.com/css2?family=Figtree:wght@400;500;600;700;800&family=Roboto+Condensed:wght@400&display=swap" rel="stylesheet">
<style>
  :root {
    --bg: #ececec;
    --card: #ffffff;
    --blue: #1b5fad;
    --ink: #1e1e1e;
    --panel: #ededed;
    --fine: #8a8a8a;
    --skin-light: #d9b49a;
    --skin-dark: #6b4330;
    --gold-light: #f4d77a;
    --gold-dark: #b7862c;
    --silver-light: #e6e6e6;
    --silver-dark: #9a9a9a;
  }
  * { box-sizing: border-box; margin: 0; padding: 0; }
  html, body { width: 1200px; height: 862px; overflow: hidden; }
  body {
    background: linear-gradient(180deg, #f2f2f2, var(--bg));
    font-family: "Figtree", sans-serif;
    color: var(--ink);
    position: relative;
  }
  .card {
    position: absolute; top: 34px; width: 530px; height: 794px;
    background: var(--card);
    box-shadow: 0 1px 4px rgba(0,0,0,.08);
  }
  .card--front { left: 61px; }
  .card--back { left: 611px; }

  .headline {
    position: absolute; left: 64px; top: 38px;
    color: var(--blue); font-weight: 700; font-size: 45px;
    line-height: 55px; letter-spacing: -1px;
  }
  .intro {
    position: absolute; left: 65px; top: 165px; width: 380px;
    font-size: 14px; line-height: 19px; font-weight: 500;
  }
  .intro p + p { margin-top: 18px; }
  .brand {
    position: absolute; display: flex; align-items: center; gap: 7px;
    font-size: 17px; font-weight: 700; color: var(--blue);
  }
  .brand__dot { width: 14px; height: 14px; border-radius: 50%; background: currentColor; }
  .brand--front { left: 64px; top: 356px; }
  .url {
    position: absolute; font-size: 13px; font-weight: 500; letter-spacing: .3px;
  }
  .url--front { left: 327px; top: 342px; }

  .photo {
    position: absolute; left: 0; top: 397px; width: 530px; height: 397px;
    background: radial-gradient(ellipse at 45% 70%, var(--skin-light), #b98466 45%, var(--skin-dark) 100%),
                linear-gradient(180deg, #e9e6e3, #cfc8c2);
    background-blend-mode: multiply;
  }
  .brand--photo { left: 64px; top: 338px; color: #fff; }
  .url--photo { left: 328px; top: 337px; color: #fff; }

  .reward {
    position: absolute; left: 42px; width: 447px; height: 150px;
    background: var(--panel);
  }
  .reward--gold { top: 42px; }
  .reward--silver { top: 203px; }
  .reward__star { position: absolute; left: 15px; top: 8px; width: 122px; height: 130px; }
  .reward__title {
    position: absolute; left: 172px; top: 26px;
    color: var(--blue); font-size: 40px; font-weight: 600; letter-spacing: .5px;
  }
  .reward__title sup { font-size: 20px; vertical-align: 18px; margin-left: 2px; }
  .reward__text {
    position: absolute; left: 171px; top: 84px; width: 260px;
    font-size: 12.5px; line-height: 19px; font-weight: 500;
  }

  .cutline {
    position: absolute; left: 42px; top: 386px; width: 460px; height: 20px;
  }
  .details {
    position: absolute; left: 64px; top: 415px; width: 410px;
    font-size: 13px; line-height: 22px; font-weight: 500;
  }
  .details strong { font-weight: 700; }
  .field {
    position: absolute; height: 39px; background: var(--panel);
    padding-left: 16px; font-size: 13px; font-weight: 500;
    display: flex; align-items: center;
  }
  .field--name { left: 43px; top: 523px; width: 444px; }
  .field--referrer { left: 43px; top: 571px; width: 444px; }
  .field--date { left: 43px; top: 619px; width: 215px; }
  .field--location { left: 268px; top: 619px; width: 219px; }
  .fineprint {
    position: absolute; left: 26px; top: 684px; width: 478px;
    font-family: "Roboto Condensed", sans-serif; font-size: 8.6px;
    line-height: 13.2px; color: var(--fine); letter-spacing: -.2px;
  }
  .fineprint .tail { display: block; width: 410px; }
  .brand--mini { left: 432px; top: 770px; font-size: 8px; gap: 4px; }
  .brand--mini .brand__dot { width: 8px; height: 8px; }
</style>
</head>
<body>
  <section class="card card--front">
    <h1 class="headline">Good people,<br>know good people.</h1>
    <div class="intro">
      <p>Referrals are the lifeblood of our small business.</p>
      <p>We are incredibly grateful for your trust and recommendations over the years, and we want to show our gratitude. That's why we are introducing an exciting new way to earn more free treatment.</p>
    </div>
    <div class="brand brand--front"><span class="brand__dot"></span>Brightpath Wellness</div>
    <div class="url url--front">www.brightpathwellness.ca</div>

    <div class="photo" role="img" aria-label="Photo of a therapist's hands giving a back massage to a client lying on a white-sheeted table">
      <div class="brand brand--photo"><span class="brand__dot"></span>Brightpath Wellness</div>
      <div class="url url--photo">www.brightpathwellness.ca</div>
    </div>
  </section>

  <section class="card card--back">
    <div class="reward reward--gold">
      <svg class="reward__star" role="img" aria-label="Gold star illustration" viewBox="0 0 122 130">
        <defs>
          <linearGradient id="gold" x1="0" y1="0" x2="1" y2="1">
            <stop offset="0" stop-color="var(--gold-light)"/><stop offset="1" stop-color="var(--gold-dark)"/>
          </linearGradient>
        </defs>
        <ellipse cx="61" cy="122" rx="40" ry="3" fill="#cfcfcf"/>
        <rect x="6" y="2" width="110" height="110" rx="50" fill="url(#gold)" opacity=".85"/>
      </svg>
      <div class="reward__title">Earn $25<sup>*</sup></div>
      <p class="reward__text">for every referral you make to our south Calgary location (Maple Ridge Drive), and;</p>
    </div>

    <div class="reward reward--silver">
      <svg class="reward__star" role="img" aria-label="Silver star illustration" viewBox="0 0 122 130">
        <defs>
          <linearGradient id="silver" x1="0" y1="0" x2="1" y2="1">
            <stop offset="0" stop-color="var(--silver-light)"/><stop offset="1" stop-color="var(--silver-dark)"/>
          </linearGradient>
        </defs>
        <ellipse cx="61" cy="122" rx="40" ry="3" fill="#cfcfcf"/>
        <rect x="6" y="2" width="110" height="110" rx="50" fill="url(#silver)" opacity=".85"/>
      </svg>
      <div class="reward__title">Earn $10<sup>*</sup></div>
      <p class="reward__text">for every referral you make to our north Calgary location (Cedar Heights).</p>
    </div>

    <svg class="cutline" viewBox="0 0 460 20" aria-hidden="true">
      <line x1="0" y1="10" x2="445" y2="10" stroke="var(--blue)" stroke-width="1.3" stroke-dasharray="8 12"/>
      <g fill="none" stroke="var(--blue)" stroke-width="1.8">
        <circle cx="483" cy="5" r="3.5" transform="translate(-28 0)"/>
        <circle cx="483" cy="15" r="3.5" transform="translate(-28 0)"/>
        <line x1="445" y1="3" x2="453" y2="13"/>
        <line x1="445" y1="17" x2="453" y2="7"/>
      </g>
    </svg>

    <p class="details">Credits can be <strong>used for any service at either our north or south location</strong> and, in the spirit of community, <strong>credits are transferable.</strong> Refer 4 people to the south and you could gift someone a $100 gift card! Or, enjoy a well deserved, free treatment yourself.</p>

    <div class="field field--name">Your name</div>
    <div class="field field--referrer">Referred by</div>
    <div class="field field--date">Date</div>
    <div class="field field--location">Location</div>

    <p class="fineprint">*Referral(s) must be brand new client(s) to the Brightpath Wellness Inc. practice, having never booked or attended an appointment at any Brightpath Wellness location. Referral must attend their appointment for you to be eligible for a referral credit. Referral credit value is dependent upon which Brightpath Wellness location your referral attends: you are eligible for a $10 credit for a referral to
      <span class="tail">our north location (#120 - 4410 Harvest Hills Way NW); you are eligible for a $25 credit for a referral to our south location (#305 - 7710 Riverbend Drive SE). We are really good at asking but please remind your referral to tell us it is YOU who we have to thank! Credit(s) may be redeemed as payment or partial payment for any service at any Brightpath Wellness location. Credits have no cash value and no expiry.</span></p>
    <div class="brand brand--mini"><span class="brand__dot"></span>Brightpath</div>
  </section>
</body>
</html>
```